mobile app design: app provides timely Natural gas pipeline information (similar to weather, etc)

we are going to create and publish an app in all the three markets.( android, ios,windows). we have wire framed mostly all the screens. the designers are to provide the layout, design & background. The following are the most important things.

1. the app's target audience are guys working in the natural gas industry in the US.
2. the app provides the customer with latest pipeline information
3. the trial version is free and will provide information about one pipeline
4. slides 1 to 5 are trial version slides.
5. slides 6 onwards the customer chooses.
6. the final product is displayed in a grid.
7. the app will be developed using html5 and css3.
8. customer will pay per pipeline for the information. ( in app payment)
9 there are similiar ( complementary) products which provide weekly storage data at vendra shelf and bramlo soft bazaar.
10. i have attached the pdf document of the wireframe.
11.i have attached the logo
12. no name has been thought out yet.

Hi guys

I have a main question for the designer community .

1. is it possible to combine some of the pages ( screens  ) into one or two. use your gut feel. if not it is ok.

2. check out the flow, the color, the background , the font and the font size. it should be pleasing.

thanx

Tomek

```html
<!DOCTYPE html>
<html lang="en">
<head>
<meta charset="utf-8">
<title>Pipeline Info – Latest</title>
<link href="https://fonts.googleapis.com/css2?family=Varela+Round&display=swap" rel="stylesheet">
<style>
  :root {
    --page-bg: #e4e4e4;
    --screen-top: #b8e2f6;
    --screen-bottom: #65a1e0;
    --accent: #3bb9e2;
    --accent-light: #e6f5fc;
    --header-teal: #4794a9;
    --header-text: #ffffff;
    --cell-bg: #eef1f1;
    --cell-border: #c5d3dc;
    --cell-text: #5c9f80;
    --status-text: #ffffff;
  }
  * { box-sizing: border-box; margin: 0; padding: 0; }
  html, body {
    width: 1200px; height: 900px; overflow: hidden;
    background: var(--page-bg);
    font-family: "Varela Round", "Helvetica Neue", Arial, sans-serif;
  }
  .app-screen {
    position: absolute; left: 380px; top: 60px;
    width: 440px; height: 780px; overflow: hidden;
    background: linear-gradient(180deg, var(--screen-top) 0%, #9fcdf0 45%, var(--screen-bottom) 100%);
  }
  .status-bar {
    height: 28px; padding: 0 10px;
    display: flex; align-items: center; justify-content: space-between;
    color: var(--status-text); font-size: 12px;
  }
  .status-left, .status-right { display: flex; align-items: center; gap: 5px; width: 130px; }
  .status-right { justify-content: flex-end; }
  .signal-dots { display: flex; gap: 2px; }
  .signal-dots span { width: 6px; height: 6px; border-radius: 50%; background: var(--status-text); }
  .signal-dots span.empty { background: none; border: 1px solid var(--status-text); }
  .status-time { font-size: 12px; }
  .battery { width: 24px; height: 11px; border: 1px solid var(--status-text); border-radius: 2px; padding: 1px; }
  .battery i { display: block; width: 100%; height: 100%; background: var(--status-text); }

  .segment-control {
    position: absolute; left: 80px; top: 46px;
    width: 280px; height: 54px; display: flex;
    border: 2px solid var(--accent); border-radius: 8px; overflow: hidden;
    font-size: 21px;
  }
  .segment { flex: 1; display: flex; align-items: center; justify-content: center; }
  .segment.is-active { background: var(--accent); color: #fff; }
  .segment.is-idle { background: var(--accent-light); color: var(--accent); }

  .pipeline-table {
    position: absolute; left: 12px; top: 122px; width: 416px;
    border-collapse: collapse; table-layout: fixed;
    font-size: 19px;
  }
  .pipeline-table th {
    background: var(--header-teal); color: var(--header-text);
    font-weight: 400; height: 38px; font-size: 18px;
    border-right: 2px solid #3d8396;
  }
  .pipeline-table td {
    background: var(--cell-bg); color: var(--cell-text);
    height: 30px; text-align: center;
    border-right: 2px solid var(--cell-border);
  }
  .pipeline-table th:last-child, .pipeline-table td:last-child { border-right: none; }
  .pipeline-table tbody tr:last-child td { border-bottom: 2px solid var(--cell-border); }

  .add-pipelines-button {
    position: absolute; left: 85px; top: 650px;
    width: 270px; height: 62px; border-radius: 10px;
    background: var(--accent); color: #fff;
    display: flex; align-items: center; justify-content: center;
    font-size: 21px; box-shadow: 0 2px 0 rgba(30, 110, 150, 0.35);
  }
</style>
</head>
<body>
  <main class="app-screen">
    <header class="status-bar">
      <div class="status-left">
        <div class="signal-dots"><span></span><span></span><span></span><span class="empty"></span><span class="empty"></span></div>
        <span class="carrier">KESTA</span>
        <svg class="wifi-icon" width="14" height="11" viewBox="0 0 14 11" aria-hidden="true">
          <path d="M1 4 A9 9 0 0 1 13 4" fill="none" stroke="#fff" stroke-width="1.5"/>
          <path d="M3.5 6.5 A5.5 5.5 0 0 1 10.5 6.5" fill="none" stroke="#fff" stroke-width="1.5"/>
          <circle cx="7" cy="9.3" r="1.4" fill="#fff"/>
        </svg>
      </div>
      <span class="status-time">4:21 PM</span>
      <div class="status-right">
        <span>100%</span>
        <div class="battery"><i></i></div>
      </div>
    </header>

    <nav class="segment-control">
      <div class="segment is-active">Latest</div>
      <div class="segment is-idle">Older</div>
    </nav>

    <table class="pipeline-table">
      <thead>
        <tr><th>region</th><th>pipeline</th><th>gasday</th><th>postingtime</th></tr>
      </thead>
      <tbody>
        <tr><td>data1</td><td>data1</td><td>data1</td><td>data1</td></tr>
        <tr><td>data1</td><td>data1</td><td>data1</td><td>data1</td></tr>
        <tr><td>data1</td><td>data1</td><td>data1</td><td>data1</td></tr>
        <tr><td>data1</td><td>data1</td><td>data1</td><td>data1</td></tr>
        <tr><td>data1</td><td>data1</td><td>data1</td><td>data1</td></tr>
        <tr><td>data1</td><td>data1</td><td>data1</td><td>data1</td></tr>
        <tr><td>data1</td><td>data1</td><td>data1</td><td>data1</td></tr>
        <tr><td>data1</td><td>data1</td><td>data1</td><td>data1</td></tr>
        <tr><td>data1</td><td>data1</td><td>data1</td><td>data1</td></tr>
        <tr><td>data1</td><td>data1</td><td>data1</td><td>data1</td></tr>
        <tr><td>data1</td><td>data1</td><td>data1</td><td>data1</td></tr>
        <tr><td>data1</td><td>data1</td><td>data1</td><td>data1</td></tr>
        <tr><td>data1</td><td>data1</td><td>data1</td><td>data1</td></tr>
      </tbody>
    </table>

    <div class="add-pipelines-button">Add More Pipelines</div>
  </main>
</body>
</html>
```